Bref créative
Business Cards, Letterhead, Envelopes, Fax Cover, Email Signature, Truck
Brindle Roofing Ltd.
I need double sided standard sized Business Card [3.5" x 2"]
Do not limit yourself to font used in logo
Professional
Tomasz Oduya
42 Fairwick Lane NE
Calgary AB T3M2R8
tomi@brindleroofing.example
www.brindleroofing.example
Open to different ideas. For example : just logo, web address etc
Photograph-1 of truck
Picture 2
Picture-3
Picture-4
Picture-5
Color scheme(s)to be used for Truck

```html
<!DOCTYPE html>
<html lang="en">
<head>
<meta charset="utf-8">
<title>Brindle Roofing Ltd. — Business Card</title>
<link rel="stylesheet" href="https://fonts.googleapis.com/css2?family=Lato:wght@400;700&family=Tinos&display=swap">
<style>
  :root {
    --backdrop: #e9e7e3;
    --card-white: #ffffff;
    --sage: #7d9c4a;
    --sage-light: #97b562;
    --sage-dark: #66843a;
    --ink: #4a4a4a;
    --ink-soft: #7a7a7a;
  }
  * { margin: 0; padding: 0; box-sizing: border-box; }
  html, body { width: 1200px; height: 720px; overflow: hidden; }
  body {
    background: var(--backdrop);
    position: relative;
    font-family: "Lato", sans-serif;
  }
  .card {
    position: absolute;
    top: 217px;
    width: 500px;
    height: 286px;
    box-shadow: 0 6px 18px rgba(0,0,0,0.18);
    overflow: hidden;
  }
  /* Front */
  .card-front { left: 70px; background: var(--card-white); }
  .front-band {
    position: absolute; left: 0; top: 0; bottom: 0; width: 100px;
    background: linear-gradient(180deg, var(--sage-light), var(--sage));
  }
  .brand {
    position: absolute; left: 112px; top: 46px;
    display: flex; align-items: center; gap: 10px;
  }
  .brand-dot {
    width: 22px; height: 22px; border-radius: 50%;
    background: var(--sage);
  }
  .brand-name {
    font-family: "Lato", sans-serif; font-weight: 700;
    font-size: 31px; color: var(--sage-dark); letter-spacing: -0.5px;
  }
  .holder {
    position: absolute; left: 128px; top: 154px;
  }
  .holder-name {
    font-family: "Tinos", serif; font-size: 15px;
    color: var(--sage-dark); letter-spacing: 0.5px; text-transform: uppercase;
  }
  .holder-licence {
    font-size: 8px; color: var(--ink-soft); margin-top: 2px;
  }
  .contact {
    position: absolute; left: 128px; top: 206px;
    font-size: 8.5px; color: var(--ink); line-height: 20px;
  }
  .contact-row { display: flex; align-items: center; gap: 14px; white-space: nowrap; }
  .contact-item { display: inline-flex; align-items: center; gap: 4px; }
  .contact-item svg { width: 8px; height: 8px; fill: var(--ink-soft); }
  /* Back */
  .card-back {
    left: 630px;
    background: radial-gradient(ellipse at 50% 45%, var(--sage-light), var(--sage) 70%, var(--sage-dark));
  }
  .back-mark {
    position: absolute; left: 50%; top: 92px; transform: translateX(-50%);
    display: flex; align-items: center; gap: 12px;
  }
  .back-dot { width: 28px; height: 28px; border-radius: 50%; background: var(--card-white); }
  .back-name {
    font-family: "Lato", sans-serif; font-weight: 700;
    font-size: 30px; color: var(--card-white); white-space: nowrap;
  }
  .back-web {
    position: absolute; left: 0; right: 0; top: 214px; text-align: center;
    font-family: "Tinos", serif; font-size: 13px; color: var(--card-white);
    letter-spacing: 0.3px;
  }
</style>
</head>
<body>
  <section class="card card-front" aria-label="Business card front">
    <div class="front-band"></div>
    <div class="brand">
      <span class="brand-dot"></span>
      <span class="brand-name">Brindle Roofing Ltd.</span>
    </div>
    <div class="holder">
      <p class="holder-name">Tomasz Oduya</p>
      <p class="holder-licence">Licence No. 4471 RF</p>
    </div>
    <div class="contact">
      <div class="contact-row">
        <span class="contact-item"><svg viewBox="0 0 10 10"><path d="M5 0a3.5 3.5 0 0 0-3.5 3.5C1.5 6 5 10 5 10s3.5-4 3.5-6.5A3.5 3.5 0 0 0 5 0zm0 5a1.5 1.5 0 1 1 0-3 1.5 1.5 0 0 1 0 3z"/></svg>42 Fairwick Lane NE Calgary AB T3M2R8</span>
      </div>
      <div class="contact-row">
        <span class="contact-item"><svg viewBox="0 0 10 10"><rect x="2" y="0" width="6" height="10" rx="1"/></svg>403 555 0142</span>
        <span class="contact-item"><svg viewBox="0 0 10 10"><rect x="0" y="2" width="10" height="7" rx="1"/></svg>403 555 0143</span>
        <span class="contact-item"><svg viewBox="0 0 10 10"><circle cx="5" cy="5" r="4"/></svg>403 555 0144</span>
        <span class="contact-item"><svg viewBox="0 0 10 10"><rect x="1" y="1" width="8" height="8"/></svg>403 555 0145</span>
      </div>
      <div class="contact-row">
        <span class="contact-item"><svg viewBox="0 0 10 10"><path d="M0 2h10v6H0z M0 2l5 3 5-3" /></svg>tomi@brindleroofing.example</span>
        <span class="contact-item"><svg viewBox="0 0 10 10"><circle cx="5" cy="5" r="4.5"/></svg>www.brindleroofing.example</span>
      </div>
    </div>
  </section>

  <section class="card card-back" aria-label="Business card back">
    <div class="back-mark">
      <span class="back-dot"></span>
      <span class="back-name">Brindle Roofing Ltd.</span>
    </div>
    <p class="back-web">www.brindleroofing.example</p>
  </section>
</body>
</html>
```